Brightpath Ventures

Marion T Haskell
"Title" Adventure Manager & Host
2871 North 42nd Street | Vancouver, BC | V5R 2B8
Direct 604.555. 0187 x 215
Chat drum41
1.800.555.0143
brightpathvx.ca
(perhaps small coastal tour bureau logo somewhere? Or “Powered by CTB”?)
- Grey/white logo cut out on reverse of card with web address

Industry/Entity Type

Travel

```html
<!DOCTYPE html>
<html lang="en">
<head>
<meta charset="utf-8">
<title>Brightpath Ventures – Business Card</title>
<link href="https://fonts.googleapis.com/css2?family=Ubuntu:wght@400;500;700&display=swap" rel="stylesheet">
<style>
  :root {
    --page: #ffffff;
    --charcoal: #4a4a4a;
    --charcoal-deep: #333333;
    --lime: #8cc63f;
    --white: #ffffff;
    --ink-grey: #4a4a4a;
  }
  * { margin: 0; padding: 0; box-sizing: border-box; }
  html, body {
    width: 1200px; height: 900px; overflow: hidden;
    background: var(--page);
    font-family: "Ubuntu", sans-serif;
  }
  .canvas { position: relative; width: 1200px; height: 900px; }

  .card-back {
    position: absolute; left: 322px; top: 43px;
    width: 590px; height: 355px;
    background: var(--charcoal);
    border-radius: 14px;
    display: flex; align-items: center; justify-content: center;
    padding-bottom: 20px;
  }
  .brand-mark { display: flex; align-items: center; gap: 14px; }
  .brand-square { width: 22px; height: 22px; background: var(--lime); }
  .brand-name {
    font-weight: 500; font-size: 30px; letter-spacing: 0.5px;
    color: var(--white);
  }

  .card-front {
    position: absolute; left: 311px; top: 466px;
    width: 591px; height: 356px;
    border-radius: 14px; overflow: hidden;
    background: var(--white);
    box-shadow: 2px 4px 8px rgba(0,0,0,0.35);
  }
  .card-front svg.card-shape { position: absolute; inset: 0; }

  .front-brand {
    position: absolute; left: 14px; top: 144px;
    display: flex; align-items: center; gap: 10px;
  }
  .front-brand .brand-square { width: 16px; height: 16px; background: var(--ink-grey); }
  .front-brand .brand-name {
    color: var(--ink-grey); font-size: 24px; line-height: 1.15;
  }

  .holder-name {
    position: absolute; left: 337px; top: 35px;
    color: var(--white); font-weight: 700; font-size: 27px;
  }
  .contact {
    position: absolute; left: 337px;
    color: var(--white); font-size: 15.5px; line-height: 20px;
  }
  .contact.address { top: 147px; }
  .contact.phones { top: 217px; left: 342px; line-height: 22.5px; }
  .contact.web { top: 294px; }
  .chat-line { display: flex; align-items: center; gap: 6px; }
  .chat-dot {
    width: 18px; height: 18px; border-radius: 50%;
    background: var(--white); display: inline-block;
  }
</style>
</head>
<body>
<main class="canvas">
  <section class="card-back" aria-label="Card reverse">
    <div class="brand-mark">
      <span class="brand-square"></span>
      <span class="brand-name">Brightpath Ventures</span>
    </div>
  </section>

  <section class="card-front" aria-label="Card front">
    <svg class="card-shape" width="591" height="356" viewBox="0 0 591 356" aria-hidden="true">
      <path d="M272 0 C322 100 336 232 196 356 L230 356 C346 232 328 100 276 0 Z" fill="var(--lime)"/>
      <path d="M276 0 C328 100 346 232 230 356 L591 356 L591 0 Z" fill="var(--charcoal-deep)"/>
    </svg>

    <div class="front-brand">
      <span class="brand-square"></span>
      <span class="brand-name">Brightpath<br>Ventures</span>
    </div>

    <h1 class="holder-name">Marion T Haskell</h1>
    <p class="contact address">Adventure Manager &amp; Host<br>2871 North 42nd Street |<br>Vancouver, BC | V5R 2B8</p>
    <div class="contact phones">
      <p>Direct 604.555. 0187 x 215</p>
      <p class="chat-line"><span class="chat-dot"></span>Chat drum41</p>
      <p>1.800.555.0143</p>
    </div>
    <p class="contact web">website: www.brightpathvx.ca</p>
  </section>
</main>
</body>
</html>
```